【依頼の目的/概要】
電子書籍(lumora)の表紙デザインをお願いします。
【画像サイズ】※QMSより抜粋
表紙ファイルの理想的な寸法は2560×1600ピクセルです。
注:画像の寸法は1000×625ピクセル以上であることが必要です。
画像の最大の寸法は10000×10000ピクセルです。

【タイトル】
「森と響きあう内なる治癒の道」
サブキャッチ
「もうガンもウイルスも怖くない」 「30年の医療現場で私が感じたこと」
「輝く人生を送るための幸せ健康学」「歴史とデータから浮かび上がる真実」など。
【著者】
看護師30年
堀田みき

【本の内容】
病院や薬に依存し続けてきた結果の日本の現状を歴史やデータから検証。
西洋医学以前の医療に着目し自然免疫の力で健康を取り戻せることが出来ることをお伝えした本です。
※本文を参考資料として添付します。

【デザイン要望】
内容が少し専門的なのですが特に一般の方に読んでいただきたいのであまり堅苦しくない印象のものを考えてはいますが、特に要望はありませんので自由な発想でのご応募を楽しみにしています。
※次点 次々点の方への参加報酬を設定いたしました。
※その他、必要な情報がありましたらお問い合わせください。
宜しくお願いいたします。

どの作品も本当に素晴らしく最後まで悩みに悩みました。内容は医療系なのですが特に一般の方に手にとっていただきたいことから表紙と内容のギャップがないものをと思うとデザインが気に入っても、本の内容で表紙のイメージと全然違うとガッカリされないかなど考え非常に悩みました。タイトルとサブキャッチの大きさや色使い、堅苦しくない明るいデザインが私のイメージと合いましたのでtorvel様のデザインを選ばせていただきました。

今回ピクモアさんに初めて表紙の依頼をさせていただきました。デザイナーさんたちのレベルの高さに感動しておりました。
どのデザインもそれぞれが個性的で本当に素晴らしく最後の最後まで迷っておりました。
今回の本の内容と、専門的ではあるのですが一般向けにしたいということで悩んだ末そちらの視点から一点決めさせていただきました。
1点しか選べないことが心苦しいです。
皆さまお忙しい中、貴重なお時間を割いていただき本当にありがとうございました。
心から感謝しております。

```html
<!DOCTYPE html>
<html lang="ja">
<head>
<meta charset="UTF-8">
<title>森と響きあう内なる治癒の道</title>
<link href="https://fonts.googleapis.com/css2?family=M+PLUS+Rounded+1c:wght@800;900&family=Noto+Sans+JP:wght@700;900&display=swap" rel="stylesheet">
<style>
  :root {
    --sky-top: #9fd2ee;
    --sky-haze: #e9f4f8;
    --forest: #3f7a4e;
    --forest-deep: #24503a;
    --lake: #5fb7b8;
    --lake-light: #cfe9e6;
    --title-orange: #f08a12;
    --title-green: #2f9a3a;
    --accent-red: #e5231b;
    --ink-brown: #4a2b12;
    --ink-dark: #2a2a2a;
    --outline: #ffffff;
  }
  * { margin: 0; padding: 0; box-sizing: border-box; }
  html, body { width: 750px; height: 1200px; overflow: hidden; background: #fff; }
  .cover {
    position: relative;
    width: 750px;
    height: 1200px;
    overflow: hidden;
    font-family: "M PLUS Rounded 1c", "Noto Sans JP", sans-serif;
  }
  .cover-photo {
    position: absolute; inset: 0;
    background:
      radial-gradient(ellipse 50% 30% at 50% 62%, rgba(255,246,220,0.75), rgba(255,246,220,0) 70%),
      linear-gradient(180deg,
        var(--sky-top) 0%,
        var(--sky-haze) 30%,
        #b9cfc4 42%,
        var(--forest) 55%,
        var(--forest-deep) 66%,
        var(--lake) 78%,
        var(--lake-light) 100%);
  }
  .vertical {
    position: absolute;
    writing-mode: vertical-rl;
    text-orientation: upright;
    white-space: nowrap;
    line-height: 1;
  }
  .tate-num { text-combine-upright: all; }
  .tagline {
    top: 28px; left: 646px;
    font-size: 42px; font-weight: 800;
    color: var(--ink-dark);
    -webkit-text-stroke: 8px var(--outline);
    paint-order: stroke fill;
    letter-spacing: 1px;
  }
  .tagline .highlight { color: var(--accent-red); }
  .title {
    font-weight: 900;
    -webkit-text-stroke: 12px var(--outline);
    paint-order: stroke fill;
  }
  .title-line-1 {
    top: 80px; left: 528px;
    font-size: 92px;
    color: var(--title-orange);
  }
  .title-line-2 {
    top: 200px; left: 410px;
    font-size: 96px;
    color: var(--title-green);
  }
  .title-badge {
    position: absolute;
    top: 790px; left: 408px;
    width: 100px; height: 100px;
    border-radius: 22px;
    background: var(--accent-red);
    border: 5px solid var(--outline);
    display: flex; align-items: center; justify-content: center;
    color: #fff;
    font-size: 76px; font-weight: 900;
  }
  .catch {
    font-family: "Noto Sans JP", sans-serif;
    font-size: 35px; font-weight: 700;
    color: var(--ink-brown);
    -webkit-text-stroke: 7px var(--outline);
    paint-order: stroke fill;
  }
  .catch-1 { top: 88px; left: 314px; }
  .catch-2 { top: 88px; left: 252px; }
  .catch-3 { top: 88px; left: 190px; }
  .author {
    position: absolute;
    left: 0; right: 0; bottom: 30px;
    text-align: center;
    font-family: "Noto Sans JP", sans-serif;
    font-weight: 900;
    color: var(--ink-brown);
    -webkit-text-stroke: 8px var(--outline);
    paint-order: stroke fill;
    white-space: nowrap;
  }
  .author-role { font-size: 38px; margin-right: 14px; }
  .author-name { font-size: 58px; letter-spacing: 6px; }
  .author-mark { font-size: 38px; margin-left: 6px; }
</style>
</head>
<body>
  <div class="cover">
    <div class="cover-photo" role="img" aria-label="山と森に囲まれた湖を背景に、両腕を空へ広げる女性の後ろ姿の写真"></div>

    <p class="vertical tagline">輝く人生を送るための<span class="highlight">幸せ健康学</span></p>

    <h1>
      <span class="vertical title title-line-1">森と響きあう</span>
      <span class="vertical title title-line-2">内なる治癒の</span>
      <span class="title-badge">道</span>
    </h1>

    <ul>
      <li class="vertical catch catch-1">・もうガンもウイルスも怖くない</li>
      <li class="vertical catch catch-2">・歴史とデータから浮かび上がる真実</li>
      <li class="vertical catch catch-3">・<span class="tate-num">30</span>年の医療現場で私が感じたこと</li>
    </ul>

    <p class="author"><span class="author-role">看護師30年</span><span class="author-name">堀田 みき</span><span class="author-mark">著</span></p>
  </div>
</body>
</html>
```